Pre-workout label and Super Greens label for Vantora Nutrition Supplements

I need a label design for Club Vantora's 2 supplements. The first is a Pre-workout. The Pre-workout label needs to be 11.25 x 2.5 inches. This label will go on a black container. The second is a Super-Green. The Super-Green label should be 11.25 x 4.25 inches and will go on a white container. We have been selling these for a few years but the current labels are a little meh. I'd like something trendier and bolder. Must keep the Club Vantora branding. All the nurtition data must appear . I attached the current designs so you can know the flavors, nutrtional data etc. Thank you!
Updates

I can upload the Club Vantora logo! If anyone can tell me how to do that.

```html
<!DOCTYPE html>
<html lang="en">
<head>
<meta charset="utf-8">
<title>Vantora Nutrition – Super Greens &amp; Pre-Workout Labels</title>
<link rel="stylesheet" href="https://fonts.googleapis.com/css2?family=Exo+2:ital,wght@1,800;1,900&family=Saira+Condensed:wght@600&family=Montserrat:ital,wght@0,600;0,700;1,700;1,800&family=Roboto:wght@400;700&display=swap">
<style>
  :root{
    --page:#cfcfcf;
    --green-bright:#6cc04a;
    --green-mid:#3f9a3e;
    --green-deep:#145a34;
    --green-ink:#0f4a2b;
    --red-bright:#e8262c;
    --red-mid:#b5151b;
    --red-deep:#4e0709;
    --red-pill:#d3242a;
    --white:#ffffff;
    --silver-a:#f4f4f4;
    --silver-b:#b9b9b9;
    --ink:#1b1b1b;
    --grey:#555;
  }
  *{box-sizing:border-box;margin:0;padding:0}
  html,body{width:794px;height:1200px;overflow:hidden;background:var(--page)}
  body{position:relative;font-family:"Montserrat",Arial,sans-serif}

  .label{position:absolute;left:20px;width:754px;overflow:hidden;color:var(--white)}
  .label--greens{top:355px;height:285px}
  .label--preworkout{top:680px;height:164px}
  .label__art{position:absolute;inset:0;width:100%;height:100%}
  .abs{position:absolute}

  /* brand lockup */
  .brand{position:absolute;left:0;right:0;text-align:center;font-family:"Saira Condensed",sans-serif;font-weight:600;letter-spacing:.06em;color:var(--white)}
  .brand__mark{display:block;margin:0 auto 3px;background:var(--white)}

  .product-title{position:absolute;left:0;right:0;text-align:center;font-family:"Exo 2",sans-serif;font-style:italic;font-weight:900;color:var(--white);line-height:.9;letter-spacing:-.01em}
  .flavor{position:absolute;text-align:center;font-family:"Exo 2",sans-serif;font-style:italic;font-weight:900;color:var(--white);letter-spacing:.01em}

  .benefit{position:absolute;display:flex;align-items:center;gap:5px}
  .benefit__text{font-family:"Montserrat",sans-serif;font-style:italic;font-weight:800;line-height:1.05;color:var(--white)}
  .benefit__sub{font-weight:600;font-style:italic;opacity:.85}

  .supplement-tag{position:absolute;font-family:"Montserrat",sans-serif;font-style:italic;font-weight:700;letter-spacing:.42em;color:var(--white)}
  .servings{position:absolute;display:flex;align-items:baseline;gap:4px;font-family:"Montserrat",sans-serif;font-style:italic;font-weight:700;color:#444}
  .servings__count{font-family:"Exo 2",sans-serif;font-weight:900;font-style:italic;color:var(--red-pill)}

  .copy{font-family:"Montserrat",sans-serif;font-weight:600;color:var(--white);line-height:1.45}

  /* supplement facts */
  .facts{position:absolute;background:var(--white);color:var(--ink);font-family:"Roboto",Arial,sans-serif;border-radius:3px}
  .facts__title{font-weight:700}
  .facts__meta{color:var(--grey)}
  .facts__row{display:grid;border-bottom:.4px solid #888}
  .facts__row--head{border-bottom:1.2px solid #222;color:var(--grey)}
  .facts__row--blend{border-bottom:.6px solid #444}
  .facts__row b{font-weight:700}
  .facts__foot{color:#333}
  .fine{position:absolute;font-family:"Roboto",Arial,sans-serif;color:var(--white)}
  .fine b{font-weight:700}
</style>
</head>
<body>

<!-- SUPER GREENS LABEL -->
<section class="label label--greens" aria-label="Super Greens label">
  <svg class="label__art" viewBox="0 0 754 285" aria-hidden="true">
    <defs>
      <linearGradient id="gBase" x1="0" y1="0" x2="0" y2="1">
        <stop offset="0" stop-color="#6ec24a"/>
        <stop offset=".45" stop-color="#3f9a3e"/>
        <stop offset=".8" stop-color="#1a6438"/>
        <stop offset="1" stop-color="#145a34"/>
      </linearGradient>
      <radialGradient id="gCenter" cx=".5" cy=".35" r=".7">
        <stop offset="0" stop-color="#95d65c"/>
        <stop offset=".6" stop-color="#5cb446"/>
        <stop offset="1" stop-color="#2f8a3c"/>
      </radialGradient>
      <linearGradient id="gSilver" x1="0" y1="0" x2="1" y2="0">
        <stop offset="0" stop-color="#f6f6f6"/>
        <stop offset=".5" stop-color="#c4c4c4"/>
        <stop offset="1" stop-color="#efefef"/>
      </linearGradient>
      <linearGradient id="gFloor" x1="0" y1="0" x2="0" y2="1">
        <stop offset="0" stop-color="#145a34" stop-opacity="0"/>
        <stop offset="1" stop-color="#0f4a2b" stop-opacity=".95"/>
      </linearGradient>
    </defs>
    <rect width="754" height="285" fill="url(#gBase)"/>
    <polygon points="182,0 516,0 540,150 525,262 180,262 165,150" fill="url(#gCenter)"/>
    <polygon points="182,0 516,0 500,10 198,10" fill="#0f4a2b"/>
    <polygon points="257,0 437,0 425,46 347,60 269,46" fill="#0f4a2b"/>
    <polyline points="269,46 347,60 425,46" fill="none" stroke="#7cd14f" stroke-width="1.5"/>
    <polygon points="165,150 540,150 525,262 180,262" fill="#1f6b3c" opacity=".55"/>
    <rect y="190" width="754" height="95" fill="url(#gFloor)"/>
    <rect y="272" width="754" height="3" fill="#7cd14f"/>
    <rect y="275" width="754" height="10" fill="url(#gSilver)"/>
    <polygon points="362,250 535,248 528,280 352,280" fill="url(#gSilver)"/>
    <!-- benefit icons -->
    <g fill="#5cb848">
      <polygon points="269,216 282,209 295,216 295,231 282,238 269,231"/>
      <polygon points="332,216 345,209 358,216 358,231 345,238 332,231"/>
      <polygon points="454,216 467,209 480,216 480,231 467,238 454,231"/>
    </g>
    <g fill="none" stroke="#fff" stroke-width="1.6" stroke-linecap="round">
      <path d="M276 221 a7 7 0 0 1 12 -1"/><path d="M288 226 a7 7 0 0 1 -12 1"/>
      <circle cx="345" cy="223.5" r="6"/><path d="M345 220 v7 M341.5 223.5 h7"/>
    </g>
    <path d="M467 231 l-6 -6 a3.5 3.5 0 0 1 6 -4 a3.5 3.5 0 0 1 6 4z" fill="#fff"/>
    <g fill="none" stroke="#7cd14f" stroke-width=".8">
      <path d="M275 240 h46"/><path d="M338 240 h106"/><path d="M460 240 h78"/>
    </g>
  </svg>

  <p class="copy abs" style="left:32px;top:47px;width:118px;font-size:5.4px">Directions: Mix one (1) scoop into 6-8oz of your favorite non-citrus juice, water, smoothie, or protein shake.</p>
  <div class="abs" style="left:23px;top:87px;width:132px;height:91px;background:rgba(255,255,255,.12);border-radius:4px"></div>
  <p class="copy abs" style="left:32px;top:97px;width:118px;font-size:5.2px">CAUTION: As with any dietary supplement, consult your healthcare practitioner before using this product, especially if you are pregnant, nursing, anticipate surgery, take medication on a regular basis or are otherwise under medical supervision. Store in a cool, dry place.<br><br>Keep out of reach of children.</p>
  <p class="copy abs" style="left:32px;top:184px;width:115px;height:48px;border:1px solid #7cd14f;border-radius:3px;padding:4px 5px;text-align:center;font-size:5px">These statements have not been evaluated by the Food and Drug Administration. This product is not intended to diagnose, treat, cure or prevent any disease.</p>

  <div class="brand" style="left:257px;right:317px;top:18px;font-size:12.5px">
    <span class="brand__mark" style="width:8px;height:8px"></span>VANTORA NUTRITION
  </div>

  <h1 class="product-title" style="left:180px;right:214px;top:80px;font-size:46px;text-shadow:0 2px 0 #2f7a35">SUPER<br>GREENS</h1>

  <div class="flavor" style="left:302px;width:190px;top:171px;height:27px;line-height:27px;font-size:15px;background:var(--red-pill);border-radius:6px;transform:skewX(-8deg)">APPLE CINNAMON</div>

  <div class="benefit" style="left:298px;top:216px"><span class="benefit__text" style="font-size:7px">DETOX<br>BODY*</span></div>
  <div class="benefit" style="left:361px;top:216px"><span class="benefit__text" style="font-size:7px">PROMOTE HEALTHY<br>DIGESTION*</span></div>
  <div class="benefit" style="left:484px;top:216px"><span class="benefit__text" style="font-size:7px">SUPPORT<br>IMMUNITY*</span></div>

  <div class="supplement-tag" style="left:203px;top:262px;font-size:6.2px">DIETARY SUPPLEMENT</div>
  <div class="servings" style="left:368px;top:252px;font-size:6.5px"><span class="servings__count" style="font-size:20px">30</span>SERVINGS 270g (9.5oz)</div>

  <div class="facts" style="left:551px;top:14px;width:189px;height:233px;padding:4px 5px;font-size:3.9px;line-height:1.2">
    <div class="facts__title" style="font-size:8.5px;line-height:1.1">Supplement Facts</div>
    <div class="facts__meta">Serving Size: Approx. 1 Scoop (9 g)<br>Servings per Container: 30</div>
    <div style="height:2px;background:#222;margin:1px 0"></div>
    <div class="facts__row facts__row--head" style="grid-template-columns:1fr 40px 16px"><span></span><span>Amount per Serving</span><span style="text-align:right">%DV</span></div>
    <div class="facts__row" style="grid-template-columns:1fr 40px 16px"><span>Calories</span><span>40</span><span></span></div>
    <div class="facts__row" style="grid-template-columns:1fr 40px 16px"><span>Total Fat</span><span>1.5 g</span><span style="text-align:right">2%</span></div>
    <div class="facts__row" style="grid-template-columns:1fr 40px 16px"><span>Total Carbohydrates</span><span>5 g</span><span style="text-align:right">2%</span></div>
    <div class="facts__row" style="grid-template-columns:1fr 40px 16px"><span>&nbsp;&nbsp;Dietary Fiber</span><span>2 g</span><span style="text-align:right">7%</span></div>
    <div class="facts__row" style="grid-template-columns:1fr 40px 16px"><span>&nbsp;&nbsp;Total Sugars</span><span>&lt;1 g</span><span></span></div>
    <div class="facts__row" style="grid-template-columns:1fr 40px 16px"><span>Protein</span><span>2 g</span><span></span></div>
    <div class="facts__row" style="grid-template-columns:1fr 40px 16px"><span>Vitamin E (as Dl-Alpha Tocopheryl Acetate)</span><span>46 mg</span><span style="text-align:right">307%</span></div>
    <div class="facts__row" style="grid-template-columns:1fr 40px 16px"><span>Calcium</span><span>30 mg</span><span style="text-align:right">2%</span></div>
    <div class="facts__row" style="grid-template-columns:1fr 40px 16px"><span>Iron</span><span>2.5 mg</span><span style="text-align:right">14%</span></div>
    <div class="facts__row" style="grid-template-columns:1fr 40px 16px"><span>Sodium</span><span>15 mg</span><span style="text-align:right">1%</span></div>
    <div class="facts__row facts__row--blend" style="grid-template-columns:1fr 40px 16px"><span>Potassium</span><span>110 mg</span><span style="text-align:right">2%</span></div>
    <div class="facts__row facts__row--blend" style="grid-template-columns:1fr 40px 16px;align-items:center"><span><b>Green Health Blend</b><br>Soy Lecithin Powder, Apple Fruit Powder, Barley Grass Powder, Alfalfa Herb Powder, Wheat Grass Powder, Wheat Sprout Powder, Barley Seed Malt Powder, Rice Bran Powder, Dulse Powder, Spinach Leaf Powder</span><span>5.8 g</span><span style="text-align:right">†</span></div>
    <div class="facts__row facts__row--blend" style="grid-template-columns:1fr 40px 16px;align-items:center"><span><b>Energy Blend*</b><br>Spirulina Whole Plant Powder, Beer Root Powder, Bee Pollen Powder, Green Tea Leaf Extract</span><span>1.41 g</span><span style="text-align:right">†</span></div>
    <div class="facts__row facts__row--blend" style="grid-template-columns:1fr 40px 16px;align-items:center"><span><b>Detox Blend*</b><br>Acerola Berry Powder, Parsley Leaf Powder, Deglycyrrhizinated (DGL) Licorice Root Powder, <i>Echinacea angustifolia</i> Herb Powder, Astragalus Root Powder, Milk Thistle Seed Extract</span><span>420 mg</span><span style="text-align:right">†</span></div>
    <div class="facts__row facts__row--blend" style="grid-template-columns:1fr 40px 16px;align-items:center"><span><b>Alkalinity Blend*</b><br>Chlorella Cracked Cell Wall Powder, Suma Root Powder, Ginkgo Leaf Extract, Grape Seed Extract</span><span>340 mg</span><span style="text-align:right">†</span></div>
    <div class="facts__row facts__row--blend" style="grid-template-columns:1fr 40px 16px;align-items:center"><span><b>Probiotic Blend Complex</b><br>Inulin, <i>Lactobacillus acidophilus, Lactobacillus bulgaricus, Bifidobacterium bifidum, Bifidobacterium longum, Streptococcus thermophilus</i></span><span>150 mg</span><span style="text-align:right">†</span></div>
    <div class="facts__row facts__row--blend" style="grid-template-columns:1fr 40px 16px;align-items:center"><span><b>Enzyme Blend</b><br>Maltodextrin, Inulin, Bromelain, Papain, Cellulase, Lipase, Protease</span><span>125 mg</span><span style="text-align:right">†</span></div>
    <div class="facts__foot">Percent Daily Values are based on a 2,000 calorie diet<br>† Daily Value (DV) not established</div>
  </div>
  <p class="fine" style="left:551px;top:249px;width:196px;font-size:3.9px;line-height:1.3"><b>Other Ingredients:</b> Organic Cassia Bark Powder, Natural Flavor, Silicon Dioxide, Rebaudioside A (From Stevia Leaf Extract), Sucralose<br>Contains: Tree Nuts (Ginkgo Nut), Wheat, and Soy<br><b>Formulated by:</b> Club Vantora, 88 Ridgeline Rd, Alder Falls, WY 82000 (555) 014-2290</p>
</section>

<!-- PRE-WORKOUT LABEL -->
<section class="label label--preworkout" aria-label="Pre-Workout label">
  <svg class="label__art" viewBox="0 0 754 164" aria-hidden="true">
    <defs>
      <linearGradient id="rBase" x1="0" y1="0" x2="0" y2="1">
        <stop offset="0" stop-color="#ec2a30"/>
        <stop offset=".55" stop-color="#c0161c"/>
        <stop offset="1" stop-color="#6d0a0d"/>
      </linearGradient>
      <radialGradient id="rCenter" cx=".5" cy=".3" r=".75">
        <stop offset="0" stop-color="#e3262c"/>
        <stop offset=".6" stop-color="#a3121a"/>
        <stop offset="1" stop-color="#5a080b"/>
      </radialGradient>
      <linearGradient id="rSilver" x1="0" y1="0" x2="1" y2="0">
        <stop offset="0" stop-color="#f6f6f6"/>
        <stop offset=".5" stop-color="#c4c4c4"/>
        <stop offset="1" stop-color="#efefef"/>
      </linearGradient>
    </defs>
    <rect width="754" height="164" fill="url(#rBase)"/>
    <polygon points="205,0 520,0 510,152 215,152" fill="url(#rCenter)"/>
    <polygon points="281,0 416,0 408,30 348,40 289,30" fill="#4e0709"/>
    <polyline points="289,30 348,40 408,30" fill="none" stroke="#ff4a4f" stroke-width="1.2"/>
    <rect y="151" width="754" height="3" fill="#ff3a40"/>
    <rect y="154" width="754" height="10" fill="url(#rSilver)"/>
    <polygon points="352,140 510,138 504,158 345,158" fill="url(#rSilver)"/>
    <g fill="#e3262c" stroke="#fff" stroke-width=".6">
      <polygon points="241,114 250,109 259,114 259,124 250,129 241,124"/>
      <polygon points="309,114 318,109 327,114 327,124 318,129 309,124"/>
      <polygon points="393,114 402,109 411,114 411,124 402,129 393,124"/>
    </g>
    <path d="M251 113 l-4 6 h3 l-1 5 l4 -6 h-3z" fill="#fff"/>
    <path d="M318 125 l-5 -5 a2.8 2.8 0 0 1 5 -3 a2.8 2.8 0 0 1 5 3z" fill="none" stroke="#fff" stroke-width="1"/>
    <path d="M397 119 h10 M398 116.5 v5 M406 116.5 v5" fill="none" stroke="#fff" stroke-width="1.2" stroke-linecap="round"/>
    <g fill="none" stroke="#ff5a5f" stroke-width=".6">
      <path d="M246 131 h45"/><path d="M314 131 h66"/><path d="M398 131 h60"/>
    </g>
  </svg>

  <div class="abs" style="left:14px;top:13px;width:168px;height:146px;background:rgba(120,8,12,.35);border-radius:3px"></div>
  <p class="copy abs" style="left:22px;top:17px;width:155px;font-size:3.6px;font-weight:700;line-height:1.4;text-align:justify">Directions: Use on training days only. Mix 1 scoop with 6-8 oz of cold water 15-30 minutes prior to training.<br><br>Warning: Not intended for use by persons under age 18. Do not exceed recommended dose. Do not consume synephrine or caffeine from other sources, including but not limited to: coffee, tea, soda, and other dietary supplements or medications containing phenylephrine or caffeine. Contains caffeine. Use in a 12 week on, 2 week off pattern. Consult your physician prior to use if you are pregnant or nursing, or if you are taking medication, including but not limited to: MAOI inhibitors, antidepressants, aspirin, non-steroidal, anti-inflammatory drugs or products containing phenylephrine, ephedrine, pseudoephedrine, or other stimulants. Consult your physician prior to use if you have a medical condition, including but not limited to: heart, liver, kidney, or thyroid disease, cardiac arrhythmia, recurrent headaches, enlarged prostate or glaucoma. Discontinue use 2 weeks prior to surgery or if you experience rapid heartbeat, dizziness, severe headaches, or shortness of breath. This product DOES NOT contain ingredients banned by certain sports organizations.</p>
  <p class="copy abs" style="left:24px;top:128px;width:148px;border:.8px solid #ff6a6e;border-radius:2px;padding:2px 4px;font-size:3.6px;font-weight:700;text-align:center;line-height:1.4">These statements have not been evaluated by the Food and Drug Administration. This product is not intended to diagnose, treat, cure or prevent any disease.</p>

  <div class="brand" style="left:281px;right:338px;top:11px;font-size:8.5px">
    <span class="brand__mark" style="width:6px;height:6px;margin-bottom:2px"></span>VANTORA NUTRITION
  </div>

  <h2 class="product-title" style="left:233px;right:289px;top:59px;font-size:24px;text-shadow:0 1.5px 0 #7a0a0e">PRE-WORKOUT</h2>

  <div class="flavor" style="left:271px;width:157px;top:87px;height:15px;line-height:15px;font-size:9.5px;background:#6cc04a;border-radius:4px;transform:skewX(-8deg)">WATERMELON SUGAR</div>

  <div class="benefit" style="left:263px;top:113px"><span class="benefit__text" style="font-size:5.3px">ENERGY*<br><span class="benefit__sub">(Caffeine)</span></span></div>
  <div class="benefit" style="left:331px;top:113px"><span class="benefit__text" style="font-size:5.3px">PERFORMANCE*<br><span class="benefit__sub">(Beta-alanine)</span></span></div>
  <div class="benefit" style="left:415px;top:113px"><span class="benefit__text" style="font-size:5.3px">STRENGTH*<br><span class="benefit__sub">(Creatine)</span></span></div>

  <div class="supplement-tag" style="left:231px;top:146px;font-size:4.8px">DIETARY SUPPLEMENT</div>
  <div class="servings" style="left:352px;top:139px;font-size:5px"><span class="servings__count" style="font-size:14px">30</span>SERVINGS 240g (8.5oz)</div>

  <div class="facts" style="left:543px;top:12px;width:194px;height:114px;padding:3px 5px;font-size:4.1px;line-height:1.22">
    <div class="facts__title" style="font-size:6.5px;line-height:1.1">Supplement Facts</div>
    <div class="facts__meta">Serving Size: 1 Scoop (8 g)<br>Servings per Container: 30</div>
    <div style="height:1.5px;background:#222;margin:1px 0"></div>
    <div class="facts__row facts__row--head" style="grid-template-columns:84px 1fr 18px"><span></span><span>Amount per Serving</span><span style="text-align:right">%DV</span></div>
    <div class="facts__row" style="grid-template-columns:84px 1fr 18px"><span>Vitamin C (Ascorbic Acid)</span><span>250mg</span><span style="text-align:right">278%</span></div>
    <div class="facts__row" style="grid-template-columns:84px 1fr 18px"><span>Vitamin B6 (as Pyridoxal-5'-Phosphate)</span><span>0.035 mg</span><span style="text-align:right">2%</span></div>
    <div class="facts__row" style="grid-template-columns:84px 1fr 18px"><span>Folate</span><span>250 mcg DFE (150 mcg Folic Acid)</span><span style="text-align:right">63%</span></div>
    <div class="facts__row" style="grid-template-columns:84px 1fr 18px"><span>Vitamin B12 (as Methylcobalamin)</span><span>20 mcg</span><span style="text-align:right">833%</span></div>
    <div class="facts__row" style="grid-template-columns:84px 1fr 18px"><span>Calcium (as Calcium Silicate)</span><span>18.30 mg</span><span style="text-align:right">1%</span></div>
    <div class="facts__row" style="grid-template-columns:84px 1fr 18px"><span>Beta-Alanine</span><span>1.5 g</span><span style="text-align:right">†</span></div>
    <div class="facts__row" style="grid-template-columns:84px 1fr 18px"><span>Creatine Monohydrate</span><span>1 g</span><span style="text-align:right">†</span></div>
    <div class="facts__row" style="grid-template-columns:84px 1fr 18px"><span>L-Arginine Alpha-Ketoglutarate</span><span>1 g</span><span style="text-align:right">†</span></div>
    <div class="facts__row" style="grid-template-columns:84px 1fr 18px"><span>L-Citrulline Malate</span><span>1 g</span><span style="text-align:right">†</span></div>
    <div class="facts__row" style="grid-template-columns:84px 1fr 18px"><span>N-Acetyl L-Tyrosine</span><span>500 mg</span><span style="text-align:right">†</span></div>
    <div class="facts__row" style="grid-template-columns:84px 1fr 18px"><span>Caffeine Anhydrous</span><span>250 mg</span><span style="text-align:right">†</span></div>
    <div class="facts__row facts__row--blend" style="grid-template-columns:84px 1fr 18px"><span>Synephrine HCl</span><span>30 mg</span><span style="text-align:right">†</span></div>
    <div class="facts__foot">† Daily Value (DV) not established</div>
  </div>
  <p class="fine" style="left:543px;top:130px;width:196px;font-size:3.7px;line-height:1.35;font-weight:700"><b>Other Ingredients:</b> Citric Acid, Pineapple Fruit Juice Powder, Silicon Dioxide, Natural and Artificial Flavors, Acesulfame Potassium, Sucralose, and FD&amp;C Red #40.<br><br>Formulated by: Club Vantora, 88 Ridgeline Rd, Alder Falls, WY 82000 (555) 014-2290</p>
</section>

</body>
</html>
```